BUSINESS CARD needed for TRAVEL BUSINESS

-Background-

Wandorvist Crew (WC) is a newly found company in Asia that trains and develops people with various demographics to become a FREQUENT TRAVELER & an ENTREPRENEUR combined. Basically, the core product that the company markets teaches people how to TRAVEL leisurely and yet EARN MONEY at the same time. Our main quote will be LIVING LIFE BY LIVING.

- The Job -

We will be constantly going out to different events, whether opening promotional booths in roadshows or at colleges or going for networking events. Thus we need a BUSINESS CARD design that portrays our POSITIONING & BRANDING

- Positioning -

TRAVEL LEISURELY & EARN at the SAME TIME

- Objective -

Serve as a BTL marketing & networking tool

- Target Audience -

Male & Females aged 19 - 35 who LOVES to TRAVEL & have strong aspirations to make it big and attaining financial freedom. The audience are enthusiastic and when they see an opportunity, they will seize it on the very spot. They are well connected and have a wide social network.

- Single Minded Proposition -

WC is My Dream Life

Target Market(s)

REFER TO CREATIVE BRIEF

Industry/Entity Type

Marketing

Requirements
Must have
• 1) The business card must portray a branding thats related to TRAVEL.

Boarding pass design was what we came up with but express your creativity and surprise me with better ideas. :)
Nice to have
• This is an idea that we have and we would most likely like to use however I do not want to restrict your creativity so i am putting in NICE TO HAVE instead.

Our idea design -> To have the namecard in the format of a BOARDING PASS lookalike

(You may refer to these weblink for inspiration -> https://www.pictofind.example/search?hl=en&q=boarding+pass&bav=on.2,or.r_gc.r_pw.r_cp.r_qf.,cf.osb&biw=1366&bih=667&um=1&ie=UTF-8&tbm=isch&source=og&sa=N&tab=wi&ei=l-f9T4KqC4fWrQfx8eC-Bg

or simply PICTOFIND BOARDING PASS IMAGES

```html
<!DOCTYPE html>
<html lang="en">
<head>
<meta charset="utf-8">
<title>Wandorvist Crew – Business Card</title>
<link rel="stylesheet" href="https://fonts.googleapis.com/css2?family=Oswald:wght@300;400;600&display=swap">
<style>
  :root {
    --ink-deep: #070a10;
    --ink-mid: #141b27;
    --ink-glow: #2a3445;
    --paper: #ffffff;
    --frame-light: #f4f6f8;
    --frame-shade: #b9c0c8;
    --shade-dark: #1a1f28;
    --sky: #2f6fc4;
    --palm: #2f6a2c;
    --sand: #f1e6d0;
    --lagoon: #3cc4c0;
  }
  * { margin: 0; padding: 0; box-sizing: border-box; }
  html, body {
    width: 686px; height: 1200px; overflow: hidden;
    background: var(--ink-deep);
  }
  .card {
    position: relative;
    width: 686px; height: 1200px;
    overflow: hidden;
    background:
      radial-gradient(ellipse 62% 42% at 50% 46%, var(--ink-glow) 0%, var(--ink-mid) 55%, var(--ink-deep) 100%);
    font-family: "Oswald", "Arial Narrow", sans-serif;
    color: var(--paper);
  }
  .tagline {
    position: absolute;
    top: 88px; left: 0; width: 100%;
    text-align: center;
    font-weight: 300;
    font-size: 70px;
    letter-spacing: 1px;
    line-height: 1;
  }
  .window {
    position: absolute;
    top: 236px; left: 93px;
    width: 500px; height: 640px;
  }
  .contact {
    position: absolute;
    top: 1010px; left: 0; width: 100%;
    text-align: center;
    font-size: 33px;
    line-height: 1.42;
    font-weight: 300;
  }
  .contact .label { font-weight: 600; }
</style>
</head>
<body>
<main class="card">
  <h1 class="tagline">LIVING LIFE BY LIVING</h1>

  <svg class="window" viewBox="0 0 500 640" xmlns="http://www.w3.org/2000/svg">
    <defs>
      <radialGradient id="window-glow" cx="50%" cy="50%" r="55%">
        <stop offset="70%" stop-color="#ffffff" stop-opacity="0.35"/>
        <stop offset="100%" stop-color="#ffffff" stop-opacity="0"/>
      </radialGradient>
      <linearGradient id="frame-fill" x1="0" y1="0" x2="1" y2="1">
        <stop offset="0%" stop-color="var(--frame-shade)"/>
        <stop offset="35%" stop-color="var(--frame-light)"/>
        <stop offset="100%" stop-color="var(--frame-light)"/>
      </linearGradient>
      <linearGradient id="view-fill" x1="0" y1="0" x2="0" y2="1">
        <stop offset="0%" stop-color="var(--sky)"/>
        <stop offset="22%" stop-color="#7fb2e6"/>
        <stop offset="38%" stop-color="var(--palm)"/>
        <stop offset="55%" stop-color="#6d8a55"/>
        <stop offset="66%" stop-color="var(--sand)"/>
        <stop offset="80%" stop-color="var(--sand)"/>
        <stop offset="100%" stop-color="var(--lagoon)"/>
      </linearGradient>
      <linearGradient id="shade-fill" x1="0" y1="0" x2="0" y2="1">
        <stop offset="0%" stop-color="#0e121a"/>
        <stop offset="100%" stop-color="var(--shade-dark)"/>
      </linearGradient>
      <clipPath id="opening">
        <rect x="42" y="64" width="416" height="516" rx="170"/>
      </clipPath>
    </defs>

    <rect class="window-glow" x="-10" y="-10" width="520" height="660" rx="230" fill="url(#window-glow)"/>
    <rect class="window-frame" x="6" y="6" width="488" height="628" rx="210" fill="url(#frame-fill)"/>

    <g clip-path="url(#opening)">
      <g role="img" aria-label="View through the window of a tropical island beach with palm trees, thatched umbrellas, loungers, a boardwalk and turquoise water">
        <rect x="42" y="64" width="416" height="516" fill="url(#view-fill)"/>
      </g>
      <path class="window-shade" d="M30 50 H470 V122 Q250 132 30 122 Z" fill="url(#shade-fill)"/>
    </g>
    <rect class="window-rim" x="42" y="64" width="416" height="516" rx="170" fill="none" stroke="#cfd5dc" stroke-width="4"/>
  </svg>

  <address class="contact" style="font-style:normal">
    <div><span class="label">Wandorvist:</span> Maren Oste</div>
    <div><span class="label">Tel:</span> 001 555 0184</div>
    <div><span class="label">Email</span> maren@wandorvist.example</div>
  </address>
</main>
</body>
</html>
```